MOLVT Study flyer

I need help designing a flyer for a research study that will include brain imaging in adolescents. The info is in the attached document. The study is called the Marrowby Orchard Lantern Vesper Trail (MOLVT) study. Ideally this would be returned as a document that I can edit in the future as we will have several new recruitment phases (different age groups, etc. I also would love to have a logo designed as part of this project, but I recognize that might be a separate design request.

```html
<!DOCTYPE html>
<html lang="en">
<head>
<meta charset="utf-8">
<title>MOLVT Study flyer</title>
<link rel="stylesheet" href="https://fonts.googleapis.com/css2?family=Barlow+Semi+Condensed:wght@500;600;700&family=Nunito+Sans:wght@400;600;700;800&family=Caveat:wght@500&display=swap">
<style>
  :root {
    --navy: #0d2660;
    --navy-deep: #0a1f52;
    --teal: #12857f;
    --teal-dark: #0b6466;
    --teal-soft: #dff2ee;
    --purple: #7a3fae;
    --purple-soft: #efe9f7;
    --lavender-tint: #f1ecf8;
    --blue: #1577c8;
    --blue-soft: #e3eefa;
    --ink: #1e2433;
    --paper: #ffffff;
    --backdrop: #808080;
  }
  * { box-sizing: border-box; margin: 0; padding: 0; }
  html, body { width: 1200px; height: 1200px; overflow: hidden; }
  body {
    background: var(--backdrop);
    font-family: "Nunito Sans", sans-serif;
    color: var(--ink);
  }
  .flyer {
    position: absolute;
    left: 210px; top: 15px;
    width: 780px; height: 1170px;
    background: var(--paper);
    overflow: hidden;
  }
  .abs { position: absolute; }

  /* Header */
  .brand-mark {
    left: 50px; top: 40px; width: 130px; height: 130px;
    border-radius: 50%; background: var(--navy);
  }
  .brand-name {
    left: 200px; top: 58px;
    font-family: "Barlow Semi Condensed", sans-serif;
    font-weight: 700; font-size: 84px; line-height: 1;
    color: var(--navy); letter-spacing: 1px;
  }
  .brand-full {
    left: 203px; top: 139px; width: 260px;
    font-family: "Barlow Semi Condensed", sans-serif;
    font-weight: 600; font-size: 17px; line-height: 21px;
    color: var(--teal); letter-spacing: .6px; text-transform: uppercase;
  }
  .study-rule { left: 203px; top: 196px; width: 254px; height: 2px; background: var(--purple); }
  .study-pill {
    left: 262px; top: 184px; width: 130px; height: 27px;
    border-radius: 14px; background: var(--purple); color: #fff;
    font-family: "Barlow Semi Condensed", sans-serif; font-weight: 600;
    font-size: 18px; letter-spacing: 6px; text-align: center; line-height: 27px;
    padding-left: 6px;
  }

  /* Photo area */
  .hero-photo { left: 410px; top: 0; width: 370px; height: 530px; }
  .brain-badge {
    left: 558px; top: 366px; width: 198px; height: 198px; border-radius: 50%;
    background: radial-gradient(circle at 50% 40%, #123a86, var(--navy-deep));
    border: 5px solid #fff;
    display: flex; flex-direction: column; align-items: center; justify-content: flex-end;
    padding-bottom: 32px; text-align: center; color: #fff;
    font-family: "Nunito Sans", sans-serif; font-weight: 600; font-size: 15.5px; line-height: 18px;
  }
  .brain-badge .highlight { color: #5ed3c4; font-weight: 700; }
  .brain-badge svg { margin-bottom: 8px; }

  /* Intro */
  .headline {
    left: 39px; top: 236px; width: 380px;
    font-family: "Barlow Semi Condensed", sans-serif; font-weight: 600;
    font-size: 42px; line-height: 46px; color: var(--navy);
  }
  .headline .age { color: var(--teal); }
  .subhead {
    left: 40px; top: 335px; width: 360px;
    font-weight: 600; font-size: 22px; line-height: 29px; color: var(--purple);
  }
  .intro {
    left: 40px; top: 404px; width: 330px;
    font-size: 14.5px; line-height: 22px; color: var(--ink);
  }
  .intro strong { color: var(--purple); font-weight: 800; }

  /* Participation */
  .section-title {
    left: 0; top: 537px; width: 780px; text-align: center; padding-right: 160px;
    font-family: "Barlow Semi Condensed", sans-serif; font-weight: 600;
    font-size: 19px; color: var(--teal-dark); letter-spacing: .3px;
  }
  .rule { height: 1.5px; background: var(--teal); top: 548px; }
  .divider { width: 0; border-left: 1.5px dotted #c7c7cf; top: 588px; height: 180px; }
  .icon-disc {
    width: 92px; height: 92px; border-radius: 50%;
    display: flex; align-items: center; justify-content: center;
  }
  .disc-teal { background: var(--teal-soft); }
  .disc-purple { background: var(--purple-soft); }
  .disc-blue { background: var(--blue-soft); }
  .step { text-align: center; font-size: 13.5px; line-height: 18.5px; color: var(--ink); }
  .step h3 {
    font-family: "Barlow Semi Condensed", sans-serif; font-weight: 600;
    font-size: 18px; line-height: 20px; text-transform: uppercase; margin-bottom: 2px;
  }
  .step-teal h3 { color: var(--teal); }
  .step-purple h3 { color: var(--purple); }
  .step-blue h3 { color: var(--blue); margin-bottom: 8px; }

  /* Eligibility */
  .eligibility {
    left: 26px; top: 790px; width: 399px; height: 228px;
    background: var(--lavender-tint); border-radius: 12px; overflow: hidden;
  }
  .eligibility h4 {
    position: absolute; left: 25px; top: 20px;
    font-family: "Barlow Semi Condensed", sans-serif; font-weight: 500;
    font-size: 17px; color: var(--purple); text-transform: uppercase;
  }
  .criteria { position: absolute; left: 24px; top: 56px; width: 230px; list-style: none; }
  .criteria li {
    display: flex; gap: 10px; align-items: flex-start;
    font-family: "Barlow Semi Condensed", sans-serif; font-weight: 500;
    font-size: 15px; line-height: 20px; margin-bottom: 16px; color: #2a2a3a;
  }
  .criteria svg { flex: 0 0 21px; margin-top: -1px; }
  .thinker { left: 245px; top: 28px; width: 148px; height: 200px; }

  /* Contact */
  .contact {
    left: 429px; top: 790px; width: 321px; height: 228px;
    background: var(--teal-dark); border-radius: 12px; color: #fff; text-align: center;
  }
  .contact h4 {
    margin-top: 28px;
    font-family: "Barlow Semi Condensed", sans-serif; font-weight: 600;
    font-size: 19px; line-height: 23px; text-transform: uppercase;
  }
  .contact .script {
    font-family: "Caveat", cursive; font-weight: 500; font-size: 33px;
    color: #c9e9e6; margin-top: 4px;
  }
  .contact-rule { position: absolute; left: 32px; top: 151px; width: 252px; height: 1px; background: #9fd1cc; }
  .contact-dot { position: absolute; left: 153px; top: 147px; width: 8px; height: 8px; border-radius: 50%; background: #fff; }
  .email-row { position: absolute; left: 22px; top: 170px; display: flex; align-items: center; gap: 12px; }
  .email-icon { width: 54px; height: 54px; border-radius: 50%; background: #fff; display: flex; align-items: center; justify-content: center; }
  .email {
    font-family: "Barlow Semi Condensed", sans-serif; font-weight: 600; font-size: 19px;
  }

  /* Footer */
  .footer { left: 0; top: 1035px; width: 780px; height: 135px; background: var(--navy); }
  .compensation {
    position: absolute; left: 46px; top: 15px; width: 314px; height: 101px;
    border: 1px dashed #2d8c89; border-radius: 4px;
  }
  .compensation .gift { position: absolute; left: 16px; top: 14px; }
  .comp-label {
    position: absolute; left: 100px; top: 8px;
    font-family: "Barlow Semi Condensed", sans-serif; font-weight: 700; color: #fff;
    font-size: 29px; line-height: 30px;
  }
  .comp-upto { position: absolute; left: 100px; top: 36px; font-family: "Barlow Semi Condensed", sans-serif; font-weight: 600; font-size: 22px; color: #fff; }
  .comp-amount {
    position: absolute; left: 166px; top: 30px;
    font-family: "Barlow Semi Condensed", sans-serif; font-weight: 700;
    font-size: 62px; line-height: 64px; color: #a66ae6;
  }
  .footer-split { position: absolute; left: 408px; top: 20px; width: 1px; height: 95px; background: #1b3674; }
  .institution { position: absolute; left: 462px; top: 34px; display: flex; align-items: center; gap: 18px; }
  .institution .mark { width: 56px; height: 62px; background: #f0c319; }
  .institution .name {
    font-family: "Barlow Semi Condensed", sans-serif; font-weight: 600;
    font-size: 30px; line-height: 32px; color: #fff;
  }
</style>
</head>
<body>
<main class="flyer">

  <!-- Header -->
  <div class="abs brand-mark" aria-hidden="true"></div>
  <div class="abs brand-name">MOLVT</div>
  <div class="abs brand-full">Marrowby Orchard Lantern Vesper Trail</div>
  <div class="abs study-rule"></div>
  <div class="abs study-pill">STUDY</div>

  <!-- Hero photo -->
  <svg class="abs hero-photo" viewBox="0 0 370 530" role="img" aria-label="Photograph of a smiling teenage girl with headphones lying on an MRI scanner bed">
    <defs>
      <linearGradient id="photoTone" x1="0" y1="0" x2="0" y2="1">
        <stop offset="0" stop-color="#dfe6ee"/>
        <stop offset=".55" stop-color="#b8c3cf"/>
        <stop offset="1" stop-color="#3a4f86"/>
      </linearGradient>
    </defs>
    <path d="M140 0 H370 V520 H120 C60 520 0 500 0 440 C0 380 50 330 50 270 C50 150 70 70 140 0 Z" fill="#8fcfc8"/>
    <path d="M150 0 H370 V515 H125 C70 515 12 495 12 440 C12 385 60 330 60 270 C60 150 80 70 150 0 Z" fill="url(#photoTone)"/>
  </svg>

  <div class="abs brain-badge">
    <svg width="58" height="50" viewBox="0 0 58 50" aria-hidden="true">
      <path d="M29 8 C22 2 10 4 8 13 C2 15 1 25 6 29 C5 36 12 41 19 39 C22 44 30 44 32 38 L34 47 M29 8 C36 2 48 4 50 13 C56 15 57 25 52 29 C53 36 46 41 39 39 C36 44 31 43 32 38" fill="none" stroke="#5ed3c4" stroke-width="2" stroke-linecap="round"/>
      <path d="M29 8 V38 M16 18 C20 20 22 24 20 28 M42 18 C38 20 36 24 38 28" fill="none" stroke="#9a7cf0" stroke-width="2" stroke-linecap="round"/>
    </svg>
    <span>Helping us<br>understand the<br><span class="highlight">developing brain</span><br>in adolescence.</span>
  </div>

  <!-- Intro -->
  <h1 class="abs headline">Are you the parent of a child age <span class="age">10–17</span>?</h1>
  <h2 class="abs subhead">Do they worry or overthink negative emotions?</h2>
  <p class="abs intro">Harrowgate University researchers are seeking <strong>girls age 10–17</strong> for a study about brain activity in emotions and decision-making and how they relate to puberty, anxiety and depression.</p>

  <!-- Participation -->
  <div class="abs rule" style="left:30px;width:104px"></div>
  <div class="abs section-title">STUDY PARTICIPATION INVOLVES:</div>
  <div class="abs rule" style="left:440px;width:140px"></div>

  <div class="abs icon-disc disc-teal" style="left:60px;top:571px">
    <svg width="60" height="54" viewBox="0 0 60 54" aria-hidden="true" fill="none" stroke="var(--navy)" stroke-width="2.4" stroke-linecap="round" stroke-linejoin="round">
      <path d="M24 6 H52 a5 5 0 0 1 5 5 V26 a5 5 0 0 1 -5 5 H50 L52 38 L44 31 H30"/>
      <path d="M6 20 H34 a5 5 0 0 1 5 5 V38 a5 5 0 0 1 -5 5 H18 L9 50 L11 43 H6 a4 4 0 0 1 -4 -4 V25 a5 5 0 0 1 4 -5 Z"/>
      <path d="M10 29 H30 M10 35 H24 M34 14 H50 M42 20 H50" stroke="var(--teal)"/>
    </svg>
  </div>
  <div class="abs step step-teal" style="left:10px;top:665px;width:192px">
    <h3>One one-hour<br>interview</h3>
    (online or in-person)<br>where your child will<br>discuss their thoughts.
  </div>

  <div class="abs divider" style="left:204px"></div>

  <div class="abs icon-disc disc-purple" style="left:243px;top:571px">
    <svg width="56" height="56" viewBox="0 0 56 56" aria-hidden="true" fill="none" stroke="var(--purple)" stroke-width="2.4" stroke-linecap="round" stroke-linejoin="round">
      <rect x="4" y="5" width="48" height="34" rx="2"/>
      <path d="M22 39 L20 49 H36 L34 39 M16 50 H40"/>
      <path d="M11 13 L13 15 L17 11 M21 13 H44 M11 21 H17 V26 H11 Z M21 22 H44 M21 30 H38" stroke="var(--navy)"/>
    </svg>
  </div>
  <div class="abs step step-purple" style="left:210px;top:671px;width:176px">
    <h3>Online<br>questionnaires</h3>
    (parent and child)
  </div>

  <div class="abs divider" style="left:386px"></div>

  <div class="abs icon-disc disc-blue" style="left:423px;top:571px">
    <svg width="64" height="50" viewBox="0 0 64 50" aria-hidden="true" fill="none" stroke="var(--navy)" stroke-width="2.4" stroke-linejoin="round">
      <rect x="4" y="6" width="26" height="38" rx="12"/>
      <circle cx="17" cy="25" r="8"/>
      <path d="M22 28 H58 V36 H10 M14 36 V44 H58 V36" />
      <path d="M34 22 H50 V28" stroke="var(--blue)"/>
    </svg>
  </div>
  <div class="abs step step-blue" style="left:510px;top:590px;width:174px">
    <h3>One two-hour<br>visit</h3>
    where your child will complete an MRI scan, answer questions about their puberty stage, and have a small hair sample taken to study puberty hormones.
  </div>
  <div class="abs icon-disc disc-teal" style="left:665px;top:571px">
    <svg width="58" height="58" viewBox="0 0 58 58" aria-hidden="true" fill="none" stroke-width="2.4" stroke-linecap="round" stroke-linejoin="round">
      <path d="M10 6 H24 M13 6 V46 a4 4 0 0 0 8 0 V6" stroke="var(--navy)"/>
      <path d="M13 28 H21 V46 a4 4 0 0 1 -8 0 Z" fill="#5ed3c4" stroke="var(--navy)"/>
      <path d="M34 50 C34 36 40 24 50 14 M32 50 a4 4 0 0 0 8 0 M40 46 H54" stroke="var(--teal)"/>
    </svg>
  </div>

  <!-- Eligibility -->
  <section class="abs eligibility">
    <h4>Your child may be eligible if they:</h4>
    <ul class="criteria">
      <li><svg width="21" height="21" viewBox="0 0 21 21" aria-hidden="true"><circle cx="10.5" cy="10.5" r="10.5" fill="var(--purple)"/><path d="M6 11 L9.2 14 L15 7.5" fill="none" stroke="#fff" stroke-width="2.2" stroke-linecap="round" stroke-linejoin="round"/></svg>Are age 10–17</li>
      <li><svg width="21" height="21" viewBox="0 0 21 21" aria-hidden="true"><circle cx="10.5" cy="10.5" r="10.5" fill="var(--purple)"/><path d="M6 11 L9.2 14 L15 7.5" fill="none" stroke="#fff" stroke-width="2.2" stroke-linecap="round" stroke-linejoin="round"/></svg>Tend to worry or overthink negative thoughts</li>
      <li><svg width="21" height="21" viewBox="0 0 21 21" aria-hidden="true"><circle cx="10.5" cy="10.5" r="10.5" fill="var(--purple)"/><path d="M6 11 L9.2 14 L15 7.5" fill="none" stroke="#fff" stroke-width="2.2" stroke-linecap="round" stroke-linejoin="round"/></svg>Have not been diagnosed with psychosis, learning problems, or autism</li>
    </ul>
    <div class="abs thinker" role="img" aria-label="Line illustration of a girl with closed eyes and a tangled thought bubble above her head" style="background: radial-gradient(circle at 40% 55%, #ddd0ef 0%, #e8dff4 45%, rgba(241,236,248,0) 72%);"></div>
  </section>

  <!-- Contact -->
  <section class="abs contact">
    <h4>Interested in participating?<br>Want more information?</h4>
    <div class="script">Please contact us!</div>
    <div class="contact-rule"></div>
    <div class="contact-dot"></div>
    <div class="email-row">
      <div class="email-icon">
        <svg width="30" height="22" viewBox="0 0 30 22" aria-hidden="true"><rect x="1" y="1" width="28" height="20" rx="2" fill="var(--navy)"/><path d="M2 2 L15 13 L28 2 M2 20 L11 11 M28 20 L19 11" fill="none" stroke="#fff" stroke-width="1.6"/></svg>
      </div>
      <span class="email">molvtstudy@harrowgate.edu</span>
    </div>
  </section>

  <!-- Footer -->
  <footer class="abs footer">
    <div class="compensation">
      <svg class="gift" width="80" height="74" viewBox="0 0 80 74" aria-hidden="true" fill="none" stroke-width="2.4" stroke-linejoin="round" stroke-linecap="round">
        <rect x="18" y="20" width="48" height="12" stroke="#5ed3c4"/>
        <path d="M22 32 V52 H62 V32 M42 20 V52" stroke="#5ed3c4"/>
        <path d="M42 20 C34 8 24 10 30 18 Z M42 20 C50 8 60 10 54 18 Z" stroke="#8a63e0"/>
        <path d="M2 56 H14 V72 H2 Z M14 58 H36 C42 58 44 64 38 64 H26 M38 64 L66 52 C72 50 74 56 70 58 L44 72 H14" stroke="#2fa8a0"/>
      </svg>
      <div class="comp-label">COMPENSATION</div>
      <div class="comp-upto">UP TO</div>
      <div class="comp-amount">$140</div>
    </div>
    <div class="footer-split"></div>
    <div class="institution">
      <div class="mark" aria-hidden="true"></div>
      <div class="name">Harrowgate<br>University</div>
    </div>
  </footer>

</main>
</body>
</html>
```